Hope KLN Disease (Non-Profit) Tri-Fold Brochure Design

We have put together the content for a brochure that we will distribute to doctors, researchers and patients about our non-profit. We would like the design of the brochure to look more professional and have nice aesthetics. It needs to incorporate all of the content in the attached Word file. We will have printed once we have a finished design.

Target Market(s)

Medical

Industry/Entity Type

Non Profit

Font styles to use
Serif
Sans Serif

Colors
33a6d7

Requirements
Must have
• Must include all content provided. Professional.
Nice to have
• Colors

```html
<!DOCTYPE html>
<html lang="en">
<head>
<meta charset="utf-8">
<title>Hope KLN Disease – Tri-Fold Brochure</title>
<link href="https://fonts.googleapis.com/css2?family=Poppins:wght@400;500;600;700;800&display=swap" rel="stylesheet">
<style>
:root{
  --blue:#33a6d7;
  --blue-dark:#1f86b8;
  --orange:#e8632a;
  --ink:#3a3a3a;
  --muted:#666;
  --paper:#ffffff;
  --stage:#dcdcdc;
  --photo-a:#c9dbe8;
  --photo-b:#7d9db8;
}
*{box-sizing:border-box;margin:0;padding:0}
html,body{width:1200px;height:1200px;overflow:hidden}
body{background:var(--stage);font-family:'Poppins',sans-serif;color:var(--ink);position:relative}
.spread{position:absolute;left:50px;width:1100px;height:545px;display:flex;background:var(--paper);box-shadow:0 6px 18px rgba(0,0,0,.18)}
.spread--outside{top:30px}
.spread--inside{top:625px}
.panel{position:relative;width:366.66px;height:100%;overflow:hidden}
.panel+.panel{border-left:1px solid #eee}
h2{font-size:15px;font-weight:700;text-transform:uppercase;line-height:1.15}
h3{font-size:12px;font-weight:700;text-transform:uppercase;color:var(--blue-dark);display:flex;align-items:center;gap:7px;margin:8px 0 5px}
p{font-size:9.4px;line-height:1.42}
.ico{width:20px;height:20px;flex:none}
.lead{font-weight:700;color:var(--blue-dark);text-transform:uppercase}

/* outside – left */
.intro{position:absolute;inset:0 0 auto 0;height:330px;background:var(--orange);color:#fff;padding:26px 24px 0}
.intro h2{margin-bottom:7px}
.intro p{margin-bottom:7px;font-size:9.2px}
.intro ul{list-style:none;font-size:9.6px;line-height:1.6}
.intro li::before{content:"";display:inline-block;width:6px;height:6px;border-radius:50%;background:#fff;margin-right:7px;vertical-align:middle}
.intro-curve{position:absolute;left:0;top:300px;width:100%;height:60px}
.pie{position:absolute;left:16px;top:372px;width:334px;height:160px}
.pie text{font-size:8px;font-weight:700;fill:var(--ink)}
.pie .lbl-left{text-anchor:end}

/* outside – middle */
.lab-photo{position:absolute;left:0;top:0;width:100%;height:170px;background:linear-gradient(135deg,var(--photo-a),var(--photo-b))}
.lab-curve{position:absolute;left:0;top:110px;width:100%;height:80px}
.support{position:absolute;left:26px;right:24px;top:190px}
.support .kicker{font-size:11px;font-weight:700;text-transform:uppercase}
.support .big{font-size:22px;font-weight:800;color:var(--orange);text-transform:uppercase;line-height:1.1;margin-bottom:6px}
.offer{font-size:12.5px;font-weight:700;color:var(--blue);line-height:1.3;margin:12px 0 12px}
.offer span{color:var(--ink);display:block}
.contact-wrap{position:relative}
.contact{list-style:none;font-size:9.5px}
.contact li{display:flex;align-items:center;gap:9px;margin-bottom:7px}
.contact svg{width:14px;height:14px;flex:none}
.seal{position:absolute;right:0;top:34px;width:44px;height:28px;border:1px solid #bbb;background:#f2f2f2}

/* outside – right */
.brand{display:flex;align-items:center;gap:8px;font-weight:700;color:var(--blue);font-size:24px}
.brand i{width:14px;height:14px;border-radius:50%;background:var(--blue);display:block}
.cover .brand{position:absolute;left:40px;top:26px}
.cover-photo{position:absolute;left:98px;top:60px;width:200px;height:200px;border-radius:50%;border:5px solid var(--blue);background:radial-gradient(circle at 40% 40%,#e8eef3,#9fb5c7)}
.history{position:absolute;left:34px;right:26px;top:290px}
.history h2{font-size:12.5px;color:var(--blue-dark);text-align:center;margin-bottom:10px}
.checks{display:grid;grid-template-columns:1fr 1fr;gap:6px 10px;font-size:10.5px;font-weight:600;margin-bottom:12px}
.checks span::before{content:"✓";display:inline-flex;align-items:center;justify-content:center;width:13px;height:13px;border-radius:50%;background:var(--blue);color:#fff;font-size:8px;margin-right:6px}
.history p{text-align:center;font-size:10px}
.cover-title{position:absolute;left:0;right:0;top:430px;text-align:center}
.cover-title strong{font-size:32px;font-weight:800;color:var(--blue)}
.cover-title p{font-size:9px;padding:0 40px}
.cover-swoosh{position:absolute;left:0;bottom:0;width:100%;height:50px}

/* inside – left */
.body-panel{padding:22px 22px 0}
.body-panel p{text-align:justify;margin-bottom:6px}
.als{position:absolute;left:0;right:0;bottom:0;height:92px;background:var(--orange);color:#fff;padding:20px 22px 0}
.als p{text-align:justify}
.als b{text-transform:uppercase}
.als-curve{position:absolute;left:0;bottom:86px;width:100%;height:20px}

/* inside – middle */
.panel--blue{background:var(--blue);color:#fff;padding:32px 28px 0}
.panel--blue h2{font-size:19px;text-align:center;line-height:1.2;margin-bottom:14px}
.panel--blue h3{color:#fff}
.panel--blue .ask{font-size:11px;font-weight:700;text-align:center;line-height:1.45;margin:26px 8px 0}
.registry{position:absolute;left:0;right:0;bottom:0;height:215px}
.registry svg{position:absolute;inset:0;width:100%;height:100%}
.registry-text{position:absolute;left:32px;right:28px;top:52px;color:var(--ink);text-align:center}
.registry-text .go{font-size:10px;font-weight:700}
.registry-text .url{font-size:12px;font-weight:700;color:var(--orange)}
.registry-text .url small{display:block;font-size:9.5px;color:var(--blue-dark)}
.registry-text p{text-align:left;margin-top:8px;font-size:9.2px}

/* inside – right */
.contacts-doc{list-style:none;font-size:9px;margin-top:6px}
.contacts-doc li{display:flex;gap:7px;margin-bottom:6px;line-height:1.35}
.contacts-doc b{color:var(--orange)}
.contacts-doc svg{width:12px;height:12px;flex:none;margin-top:2px}
.media-row{position:absolute;left:0;right:0;top:212px;height:120px;display:flex}
.logo-block{width:42%;background:var(--orange);display:flex;align-items:center;justify-content:center}
.logo-block .brand{color:#fff;font-size:19px}
.logo-block .brand i{background:#fff}
.protein{flex:1;background:radial-gradient(circle at 50% 50%,#2b7fb3,#0b1f33)}
.treat{position:absolute;left:22px;right:22px;top:355px}
.treat p{text-align:justify;margin-bottom:6px}
</style>
</head>
<body>

<section class="spread spread--outside">
  <div class="panel">
    <div class="intro">
      <h2>What is IBMPFD?</h2>
      <p>Inclusion Body Myopathy associated with Paget's disease of bone and Frontotemporal Dementia is an autosomal dominant disorder caused by a mutation in the KLN (Valosin Containing Protein) gene. Given the interaction with other genetic diseases, this mutation may also be known as KLN Disease or Disorder.</p>
      <p>Some patients have familial Amyotrophic Lateral Sclerosis (ALS or Lou Gehrig's disease) or Parkinson's which has been shown to have a pathogenic variant in KLN.</p>
      <h2>Penetrance by phenotype</h2>
      <p>The frequency that IBMPFD or KLN Disease manifests itself in one, two, or three primary disorders.</p>
      <ul>
        <li>IBM: Inclusion Body Myopathy</li>
        <li>PDB: Paget's Disease of the Bone</li>
        <li>FTD: Frontotemporal Dementia</li>
      </ul>
    </div>
    <svg class="intro-curve" viewBox="0 0 367 60" preserveAspectRatio="none"><path d="M0 0H367V10C260 60 110 20 0 50Z" fill="#e8632a"/></svg>
    <svg class="pie" viewBox="0 0 334 160" role="img" aria-label="Pie chart of penetrance by phenotype">
      <g transform="translate(162 82) rotate(-90)">
        <circle r="30" fill="none" stroke="#9a9a9a" stroke-width="60" pathLength="100" style="stroke-dasharray:45 55;stroke-dashoffset:0"/>
        <circle r="30" fill="none" stroke="#f6b800" stroke-width="60" pathLength="100" style="stroke-dasharray:27 73;stroke-dashoffset:-45"/>
        <circle r="30" fill="none" stroke="#3fb6a8" stroke-width="60" pathLength="100" style="stroke-dasharray:3 97;stroke-dashoffset:-72"/>
        <circle r="30" fill="none" stroke="#8cc63f" stroke-width="60" pathLength="100" style="stroke-dasharray:5 95;stroke-dashoffset:-75"/>
        <circle r="30" fill="none" stroke="#cfe8f3" stroke-width="60" pathLength="100" style="stroke-dasharray:3 97;stroke-dashoffset:-80"/>
        <circle r="30" fill="none" stroke="#2a58a8" stroke-width="60" pathLength="100" style="stroke-dasharray:7 93;stroke-dashoffset:-83"/>
        <circle r="30" fill="none" stroke="#e8632a" stroke-width="60" pathLength="100" style="stroke-dasharray:10 90;stroke-dashoffset:-90"/>
      </g>
      <text x="228" y="36">IBM,PDB AND FTD-10%</text>
      <text x="230" y="56">IBM &amp; FTD-7%</text>
      <text x="230" y="130">IBM ONLY-45%</text>
      <text class="lbl-left" x="96" y="30">FTD ONLY-3%</text>
      <text class="lbl-left" x="94" y="50">PDB ONLY-5%</text>
      <text class="lbl-left" x="94" y="70">PDB &amp; FTD-3%</text>
      <text class="lbl-left" x="96" y="112">IBM &amp; PDB-27%</text>
    </svg>
  </div>

  <div class="panel">
    <div class="lab-photo" role="img" aria-label="Photo of a researcher at a laboratory microscope"></div>
    <svg class="lab-curve" viewBox="0 0 367 80" preserveAspectRatio="none">
      <path d="M0 80V40C120 70 250 50 367 0V80Z" fill="#fff"/>
      <path d="M0 40C120 70 250 50 367 0" fill="none" stroke="#e8632a" stroke-width="4"/>
    </svg>
    <div class="support">
      <div class="kicker">Together we can make</div>
      <div class="big">A Difference</div>
      <h3><svg class="ico" viewBox="0 0 20 20"><circle cx="10" cy="10" r="10" fill="#33a6d7"/><circle cx="10" cy="7.5" r="3" fill="#fff"/><path d="M4.5 15c1-3 3-4 5.5-4s4.5 1 5.5 4z" fill="#fff"/></svg>Patient Support</h3>
      <p>Hope KLN Disease, Inc. is a 501(c)(3) which was formed to drive efforts to cure diseases related to mutations of the Valosin Containing Protein (KLN) gene. Our main goal is to bring patients and doctors together so we can help one another and drive research towards a cure. We are also trying to bring awareness to the medical community about our rare disease.</p>
      <p class="offer">We offer resources and support to patients, caregivers and doctors.<span>Connect with us.</span></p>
      <div class="contact-wrap">
        <ul class="contact">
          <li><svg viewBox="0 0 14 14"><rect width="14" height="14" rx="3" fill="#33a6d7"/></svg>IBMPFD Social page<br>HopeKLN.org | ibmpfd-info.org</li>
          <li><svg viewBox="0 0 14 14"><path d="M7 0a5 5 0 0 0-5 5c0 4 5 9 5 9s5-5 5-9a5 5 0 0 0-5-5zm0 7a2 2 0 1 1 0-4 2 2 0 0 1 0 4z" fill="#555"/></svg>Hope KLN Disease Inc. P.O. Box 4120<br>Lakeview, ST 30000</li>
          <li><svg viewBox="0 0 14 14"><rect y="2" width="14" height="10" rx="1.5" fill="#555"/><path d="M1 3l6 5 6-5" fill="none" stroke="#fff" stroke-width="1.3"/></svg>hopekln@mailbox.org</li>
          <li><svg viewBox="0 0 14 14"><circle cx="7" cy="7" r="6" fill="none" stroke="#555" stroke-width="1.4"/><path d="M1 7h12M7 1c-3 3-3 9 0 12M7 1c3 3 3 9 0 12" fill="none" stroke="#555" stroke-width="1"/></svg>www.hopekln.org</li>
        </ul>
        <div class="seal"></div>
      </div>
    </div>
  </div>

  <div class="panel cover">
    <div class="brand"><i></i>Hope KLN</div>
    <div class="cover-photo" role="img" aria-label="Photo of a gloved hand using a laboratory pipette"></div>
    <div class="history">
      <h2>Do you have a family history<br>of adult onset</h2>
      <div class="checks">
        <span>Muscle Weakness?</span><span>ALS?</span>
        <span>Dementia?</span><span>Parkinson's?</span>
        <span>Bone Disease?</span><span>IBM?</span>
      </div>
      <p>You may consider talking to your doctor about a mutation of the KLN gene called</p>
    </div>
    <div class="cover-title">
      <strong>IBMPFD</strong>
      <p>Inclusion Body Myopathy associated with Paget's Disease of Bone and Frontotemporal Dementia</p>
    </div>
    <svg class="cover-swoosh" viewBox="0 0 367 50" preserveAspectRatio="none"><path d="M0 50V30C120 0 250 40 367 10V50Z" fill="#33a6d7"/></svg>
  </div>
</section>

<section class="spread spread--inside">
  <div class="panel body-panel">
    <h3><svg class="ico" viewBox="0 0 20 20"><circle cx="10" cy="10" r="10" fill="#33a6d7"/><path d="M6 5v5a4 4 0 0 0 8 0V5" fill="none" stroke="#fff" stroke-width="1.6"/></svg>Symptoms</h3>
    <p>IBMPFD, a KLN Disease, is an adult onset disorder that can affect the muscles, bones, and brain, and an affected patient may have any combination of the following conditions.</p>
    <p><span class="lead">Inclusion Body Myopathy:</span> The first symptom of IBMPFD is often muscle weakness (myopathy). Typically, patients first notice difficulty raising arms, losing balance or difficulty climbing stairs. As the disorder progresses, weakness develops in the other muscles in the arms, legs and core muscles. Muscle weakness can also affect respiratory and heart (cardiac) muscles. This disorder may first present in an individual's late 30's and over time occurs in approximately 90% of individuals with KLN Disease.</p>
    <h3><svg class="ico" viewBox="0 0 20 20"><circle cx="10" cy="10" r="10" fill="#33a6d7"/><path d="M5 13l3-4 3 2 4-5" fill="none" stroke="#fff" stroke-width="1.6"/></svg>Penetrance by phenotype</h3>
    <p><span class="lead">Paget's Disease of Bone:</span> Bone pain, particularly in the hips and spine, is usually the major symptom of Paget's disease. It most often affects bones of the hips, spine, and skull and the long bones of the arms and legs. Paget's disease affects half of individuals with KLN Disease and typically first presents in a person's 30's or 40's, which is a much earlier age than those without KLN Disease.</p>
    <p><span class="lead">Frontotemporal Dementia:</span> In about one-third of people with KLN Disease, the disorder also affects the brain. FTD typically changes personality, behavior, language and speech. FTD typically presents in the mid-50's.</p>
    <svg class="als-curve" viewBox="0 0 367 20" preserveAspectRatio="none"><path d="M0 20V8C120 0 250 16 367 4V20Z" fill="#33a6d7"/></svg>
    <div class="als">
      <p><b>Amyotrophic Lateral Sclerosis (ALS or Lou Gehrig's Disease):</b> ALS occurs in approximately 10% of individuals with KLN Disease. Symptoms include increased muscle tone, weakness, muscle wasting, muscle cramps.</p>
    </div>
  </div>

  <div class="panel panel--blue">
    <h2>Strength through numbers will help us find a cure!</h2>
    <h3><svg class="ico" viewBox="0 0 20 20"><circle cx="10" cy="10" r="10" fill="#fff"/><circle cx="7" cy="8" r="2" fill="#33a6d7"/><circle cx="13" cy="8" r="2" fill="#33a6d7"/><path d="M4 14c1-2 5-2 6 0M10 14c1-2 5-2 6 0" fill="none" stroke="#33a6d7" stroke-width="1.4"/></svg>Research</h3>
    <p>The goal of the RareLink registry is to connect as many patients and researchers as possible to help advance treatments and cures for rare diseases.</p>
    <p class="ask">If you have been diagnosed with IBMPFD or KLN Disease, please help us by completing the patient registry through RareLink.</p>
    <div class="registry">
      <svg viewBox="0 0 367 215" preserveAspectRatio="none"><path d="M0 215V40C60 -10 300 -10 367 40V215Z" fill="#fff"/><path d="M0 40C60 -10 300 -10 367 40" fill="none" stroke="#1f86b8" stroke-width="3"/></svg>
      <div class="registry-text">
        <div class="go">Go to our website</div>
        <div class="url">www.hopekln.org<small>to access the RareLink Registry</small></div>
        <p>The RareLink registry is free for patients to enroll and for researchers to access.</p>
        <p>Please elect for researchers to have access to your registry, as that will greatly assist in the drive for a cure, especially when drug trials are recruiting patients.</p>
      </div>
    </div>
  </div>

  <div class="panel body-panel">
    <h3><svg class="ico" viewBox="0 0 20 20"><circle cx="10" cy="10" r="10" fill="#33a6d7"/><path d="M6 10l3 3 5-6" fill="none" stroke="#fff" stroke-width="1.8"/></svg>Diagnosis</h3>
    <p>The only way of diagnosing KLN Disease is through genetic testing. Consult with your doctor about testing for mutations of the KLN gene.</p>
    <p>For information about genetic testing, our two medical advisors are available as resources:</p>
    <ul class="contacts-doc">
      <li><svg viewBox="0 0 12 12"><circle cx="6" cy="6" r="6" fill="#e8632a"/></svg><span><b>Dr. Elena Marsh,</b> Medical Geneticist at Westbrook University<br>emarsh@westbrook.edu</span></li>
      <li><svg viewBox="0 0 12 12"><circle cx="6" cy="6" r="6" fill="#e8632a"/></svg><span><b>Dr. Paul Aldren,</b> Neuromuscular Specialist at Northfield University<br>paldren@northfield.edu</span></li>
    </ul>
    <div class="media-row">
      <div class="logo-block"><div class="brand"><i></i>Hope KLN</div></div>
      <div class="protein" role="img" aria-label="Illustration of a protein molecular structure"></div>
    </div>
    <div class="treat">
      <h3><svg class="ico" viewBox="0 0 20 20"><circle cx="10" cy="10" r="10" fill="#33a6d7"/><path d="M10 5v10M5 10h10" stroke="#fff" stroke-width="2"/></svg>Treatments:</h3>
      <p>There is an approved treatment for Paget's disease of bone, so early testing for this disorder is very important.</p>
      <p>There are no known cures or treatments for the Inclusion Body Myopathy or Frontotemporal Dementia. Consult with your doctor about physical therapy, stretching, diet and mobility.</p>
    </div>
  </div>
</section>

</body>
</html>
```